Harvest Gate Fellowship Network needs a fresh new web design

We are an up and coming multicultural church that aims to bring people into a life changing encounter with God. We need a fresh and inviting website in order to increase our internet presence and make us easier to connect with.
Here are some of the basic requirements for the site:
• Clearly displayed address, service times, and contact info
• A staff profile page
• An area for a calendar with upcoming events and their details
• Social media buttons
• Group pages for the different ministries (youth, children’s church, men, etc…)
• An area for donations and eCommerce
• A resources page for assorted media (podcasts, sermons, videos, etc.…)
• An area for prayer requests.

Industry/Entity Type

Church

```html
<!DOCTYPE html>
<html lang="en">
<head>
<meta charset="utf-8">
<title>Harvest Gate Fellowship Network</title>
<link rel="stylesheet" href="https://fonts.googleapis.com/css2?family=Open+Sans:wght@400;600;700;800&family=Arimo:wght@400;700&family=Libre+Baskerville&display=swap">
<style>
:root{
  --purple:#2d0c8c;
  --violet:#4511c6;
  --violet-deep:#2a0a7e;
  --amber:#f7ab02;
  --amber-text:#e8a317;
  --gold-btn:#b48b12;
  --green:#29c06b;
  --green-text:#239a53;
  --ink:#444;
  --body:#333;
  --muted:#777;
  --page:#ebebeb;
  --panel:#fff;
  --footer:#1d1d1d;
  --footer-base:#121212;
  --footer-text:#9a9a9a;
}
*{box-sizing:border-box;margin:0;padding:0}
html,body{width:900px;height:1200px;overflow:hidden;background:#fff}
body{position:relative;font-family:'Arimo',Arial,sans-serif;color:var(--body)}
.abs{position:absolute}

.topline{left:0;top:0;width:900px;height:4px;background:var(--purple)}
.brand{left:76px;top:16px;display:flex;align-items:center;gap:8px}
.brand-dot{width:52px;height:52px;border-radius:50%;background:var(--purple);flex:none}
.brand-name{font-family:'Open Sans',sans-serif;font-weight:700;font-size:17px;line-height:19px;color:var(--purple);width:170px}
.callus{right:78px;top:12px;font-family:'Open Sans',sans-serif;font-size:10px;color:#999;letter-spacing:.3px}
.callus b{font-size:13.5px;color:var(--violet);font-weight:600;letter-spacing:0}
.callus .slash{color:#bbb;font-size:13px}
.nav{left:400px;top:60px;display:flex;font-family:'Open Sans',sans-serif;font-size:12px;color:#444}
.nav span{padding:0 14px;height:21px;line-height:21px;border-left:1px solid #ddd}
.nav span:first-child{border-left:none}

.hero{left:0;top:88px;width:900px;height:360px;background:linear-gradient(180deg,#cfe3e6 0%,#b9d7d2 45%,#a9c9a4 75%,#8fae8c 100%)}

.page{left:0;top:448px;width:900px;height:542px;background:var(--page)}

.welcome{left:75px;top:466px;width:559px;height:200px;background:var(--panel);box-shadow:0 6px 8px -6px rgba(0,0,0,.25)}
.welcome h1{position:absolute;left:9px;top:20px;width:150px;font-family:'Open Sans',sans-serif;font-weight:800;font-size:23px;line-height:30px;color:#4a4a4a;letter-spacing:-.3px}
.welcome h1 span{display:block;white-space:nowrap}
.welcome h1 .sm{font-size:19px;font-weight:700}
.welcome h2{position:absolute;left:169px;top:18px;font-family:'Open Sans',sans-serif;font-weight:700;font-size:13.5px;color:var(--violet-deep)}
.welcome p{position:absolute;left:169px;width:378px;font-size:9px;line-height:15px;color:var(--body);text-align:justify}
.welcome .p1{top:42px}
.welcome .p2{top:148px}

.calendar{left:659px;top:462px;width:163px;height:166px;background:#fff;border:1px solid #ccc}
.cal-head{height:26px;background:var(--violet);color:#fff;font-weight:700;font-size:10px;text-align:center;line-height:26px;position:relative}
.cal-head i{position:absolute;top:0;font-style:normal;font-size:8px;color:#b9a3ff}
.cal-grid{display:grid;grid-template-columns:repeat(7,23.2px);grid-auto-rows:23.2px;font-size:9px;text-align:center;line-height:23.2px;color:#222}
.cal-grid span{border-right:1px solid #e3e3e3;border-bottom:1px solid #e3e3e3}
.cal-grid .dow{color:#888;font-size:8.5px;border:none;line-height:18px}
.cal-grid .we{background:#f3f3f3}
.cal-grid .off{color:#aaa}
.cal-grid .hl{background:var(--violet);color:#fff;font-weight:700}
.cal-grid .today{background:var(--green);color:#fff;font-weight:700}
.events-btn{left:659px;top:640px;width:163px;height:24px;background:var(--violet);color:#fff;font-size:12.5px;text-align:center;line-height:24px;letter-spacing:.3px}

.card{width:219px;height:258px;top:696px;background:var(--panel);box-shadow:0 0 3px rgba(0,0,0,.1)}
.card-head{height:56px;background:linear-gradient(180deg,#fff,#f0f0f0);border-bottom:1px solid #e5e5e5}
.badge{position:absolute;width:62px;height:62px;border-radius:50%;top:-9px;left:1px;border:3px solid #fff}
.badge svg{width:62px;height:62px;position:absolute;left:-3px;top:-3px}
.card-title{position:absolute;font-family:'Arimo',Arial,sans-serif;font-weight:700;font-size:19px;line-height:19px}
.staff{left:77px}
.ministries{left:333px}
.prayer{left:588px}
.staff .badge{background:var(--amber)}
.ministries .badge{background:var(--violet-deep)}
.prayer .badge{background:var(--green)}
.staff .card-title{left:77px;top:21px;color:var(--amber-text)}
.ministries .card-title{left:77px;top:21px;color:var(--violet-deep)}
.prayer .card-title{left:73px;top:8px;color:var(--green)}

.person{position:absolute;left:13px;display:flex;gap:9px}
.person .thumb{width:80px;height:58px;border:2px solid #fff;outline:1px solid #ddd;background:linear-gradient(135deg,#c9a98a,#8f6e5b 50%,#d8bfa7)}
.person h3{font-family:'Libre Baskerville',serif;font-weight:400;font-size:14px;color:#444;margin-top:10px}
.person p{font-size:9px;line-height:13.5px;color:#555;margin-top:3px}
.rule{position:absolute;left:0;width:219px;height:1px;background:#e9e9e9}

.photo{position:absolute;left:12px;top:74px;width:196px;height:88px;border:3px solid #fff;outline:1px solid #ddd}
.ministries .photo{background:linear-gradient(120deg,#c98a56,#e2b48a 40%,#5b4a44 70%,#2e2a2a)}
.prayer .photo{background:linear-gradient(100deg,#8a6a3e,#d7c9b0 45%,#e9dfcf 70%,#b59a6a)}
.card h4{position:absolute;left:12px;top:176px;font-size:10.5px;font-weight:700}
.ministries h4{color:var(--violet-deep)}
.prayer h4{color:var(--green-text)}
.card .blurb{position:absolute;left:12px;top:192px;width:200px;font-size:9px;line-height:13.5px;color:#555}

.btn{position:absolute;height:22px;line-height:22px;font-size:11px;font-weight:700;color:#fff;text-align:center;border:1px solid #fff;outline:1px solid #ccc}
.btn.gold{left:142px;top:944px;width:84px;background:var(--gold-btn)}
.btn.purple{background:var(--violet-deep);width:83px;top:943px}

.footer{left:0;top:990px;width:900px;height:166px;background:var(--footer)}
.footer-base{left:0;top:1156px;width:900px;height:44px;background:var(--footer-base)}
.f-title{position:absolute;top:1017px;font-family:'Open Sans',sans-serif;font-size:13px;color:#bdbdbd}
.f-divider{position:absolute;top:1022px;width:1px;height:104px;background:#333}
.f-link{position:absolute;font-family:'Open Sans',sans-serif;font-size:10.5px;color:var(--footer-text)}
.f-link::before{content:"›";margin-right:6px;color:#777}
.social{position:absolute;left:380px;display:flex;align-items:center;gap:11px;font-family:'Open Sans',sans-serif;font-size:10.5px;color:var(--footer-text)}
.social i{width:20px;height:20px;display:block}
.f-brand{left:612px;top:1040px;display:flex;align-items:center;gap:5px}
.f-brand .dot{width:24px;height:24px;border-radius:50%;background:#bbb}
.f-brand span{font-family:'Open Sans',sans-serif;font-weight:700;font-size:9px;line-height:11px;color:#ddd;width:100px}
.f-info{position:absolute;left:614px;display:flex;align-items:center;gap:6px;font-family:'Open Sans',sans-serif;color:var(--footer-text)}
.donate{left:78px;top:1175px;font-size:9px;color:#888}
.pay{position:absolute;top:1168px;width:35px;height:22px;border-radius:2px;font-size:6.5px;font-weight:700;text-align:center;line-height:22px}
.copy{right:86px;top:1175px;font-size:9px;color:#777}
</style>
</head>
<body>
<div class="abs topline"></div>

<header>
  <div class="abs brand"><div class="brand-dot"></div><div class="brand-name">Harvest Gate Fellowship Network</div></div>
  <div class="abs callus">CALL US: <b>555-218-4470</b> <span class="slash">/</span> <b>555-306-9152</b></div>
  <nav class="abs nav"><span>Who we are</span><span>What we do</span><span>Get Involved</span><span>News</span><span>Contact Us</span></nav>
</header>

<div class="abs hero" role="img" aria-label="Photo of a smiling boy and young woman sitting together in a tree on a sunny lawn"></div>

<main>
  <div class="abs page"></div>

  <section class="abs welcome">
    <h1><span>WELCOME TO</span><span>HARVEST</span><span>GATE</span><span class="sm">FELLOWSHIP</span><span>NETWORK</span></h1>
    <h2>Simply dummy text of the printing and typesetting</h2>
    <p class="p1">Lorem Ipsum is simply dummy text of the printing and typesetting industry. Lorem Ipsum has been the industry's standard dummy text ever since the 1500s, when an unknown printer took a galley of type and scrambled it to make a type specimen book. It has survived not only five centuries, but also the leap into electronic typesetting, remaining essentially unchanged. It was popularised in the 1960s with the release of Lettersheet sheets containing Lorem Ipsum passages, and more recently with desktop.</p>
    <p class="p2">Lettersheet sheets containing Lorem Ipsum passages, and more recently with desktop publishing software like Alden PageBuilder including versions of Lorem Ipsum.</p>
  </section>

  <aside class="abs calendar">
    <div class="cal-head"><i style="left:16px">‹</i>February 2013<i style="right:10px">›</i></div>
    <div class="cal-grid">
      <span class="dow">M</span><span class="dow">T</span><span class="dow">W</span><span class="dow">T</span><span class="dow">F</span><span class="dow">S</span><span class="dow">S</span>
      <span class="off">28</span><span>1</span><span class="hl">2</span><span>3</span><span>4</span><span class="we">5</span><span class="we">6</span>
      <span>7</span><span>8</span><span>9</span><span>10</span><span>11</span><span class="hl">12</span><span class="we">13</span>
      <span>14</span><span class="today">15</span><span>16</span><span>17</span><span class="hl">18</span><span class="we">19</span><span class="we">20</span>
      <span>21</span><span>22</span><span>23</span><span>24</span><span>25</span><span class="hl">26</span><span class="we">27</span>
      <span>28</span><span>29</span><span>30</span><span>31</span><span class="off">1</span><span class="off we">2</span><span class="off we">3</span>
    </div>
  </aside>
  <div class="abs events-btn">UPCOMING EVENTS</div>

  <section class="abs card staff">
    <div class="card-head"></div>
    <div class="badge"><svg viewBox="0 0 62 62"><circle cx="31" cy="26" r="8" fill="#fff"/><path d="M17 44c0-8 6-12 14-12s14 4 14 12z" fill="#fff"/></svg></div>
    <div class="card-title">OUR STAFF</div>
    <div class="person" style="top:76px"><div class="thumb" role="img" aria-label="Group photo of smiling children"></div><div><h3>Lorem Ipsum</h3><p>Etiam porta sem<br>malesuada magna...</p></div></div>
    <div class="rule" style="top:150px"></div>
    <div class="person" style="top:166px"><div class="thumb" role="img" aria-label="Group photo of smiling children"></div><div><h3>Lorem Ipsum</h3><p>Etiam porta sem<br>malesuada magna...</p></div></div>
    <div class="rule" style="top:240px"></div>
  </section>
  <div class="btn gold">VIEW MORE</div>

  <section class="abs card ministries">
    <div class="card-head"></div>
    <div class="badge"><svg viewBox="0 0 62 62"><path d="M19 27h24l-12-8z" fill="#fff"/><rect x="20" y="29" width="22" height="12" fill="none" stroke="#fff" stroke-width="1.5"/><path d="M24 30v10M28 30v10M32 30v10M36 30v10" stroke="#fff" stroke-width="1.5"/><rect x="17" y="42" width="28" height="3" fill="#fff"/></svg></div>
    <div class="card-title">MINISTRIES</div>
    <div class="photo" role="img" aria-label="Photo of a boy writing at a desk"></div>
    <h4>Porta Nibh Pharetra Quam Inceptos</h4>
    <p class="blurb">Aenean eu leo quam. Pellentesque ornare sem lacinia quam venenatis vestibulum. Vivamus sagittis lacus vel augue laoreet rutrum faucibus.</p>
  </section>
  <div class="btn purple" style="left:399px">READ MORE</div>

  <section class="abs card prayer">
    <div class="card-head"></div>
    <div class="badge"><svg viewBox="0 0 62 62"><circle cx="29" cy="20" r="4.5" fill="#fff"/><path d="M27 27l6 6-8 5h14" fill="none" stroke="#fff" stroke-width="4" stroke-linecap="round" stroke-linejoin="round"/></svg></div>
    <div class="card-title">PRAYER<br>REQUESTS</div>
    <div class="photo" role="img" aria-label="Photo of a woman with bowed head in quiet prayer"></div>
    <h4>Porta Nibh Pharetra Quam Inceptos</h4>
    <p class="blurb">Aenean eu leo quam. Pellentesque ornare sem lacinia quam venenatis vestibulum. Vivamus sagittis lacus vel augue laoreet rutrum faucibus.</p>
  </section>
  <div class="btn purple" style="left:654px">READ MORE</div>
</main>

<footer>
  <div class="abs footer"></div>
  <div class="f-title" style="left:78px">QUICK LINKS</div>
  <div class="f-link" style="left:78px;top:1050px">Home</div>
  <div class="f-link" style="left:78px;top:1072px">Board</div>
  <div class="f-link" style="left:78px;top:1094px">About Us</div>
  <div class="f-link" style="left:78px;top:1115px">Mission</div>
  <div class="f-link" style="left:177px;top:1050px">Sponsors</div>
  <div class="f-link" style="left:177px;top:1072px">Events</div>
  <div class="f-link" style="left:177px;top:1094px">Contact</div>
  <div class="f-divider" style="left:302px"></div>

  <div class="f-title" style="left:379px">FOLLOW US</div>
  <div class="social" style="top:1051px"><i style="background:#3b5a9a"></i>Friendspace</div>
  <div class="social" style="top:1079px"><i style="background:#d8282a"></i>Streamview</div>
  <div class="social" style="top:1106px"><i style="background:#2aa3e0"></i>Chirpline</div>
  <div class="f-divider" style="left:534px"></div>

  <div class="f-title" style="left:614px">GET IN TOUCH</div>
  <div class="abs f-brand"><div class="dot"></div><span>Harvest Gate Fellowship Network</span></div>
  <div class="f-info" style="top:1074px;font-size:10.5px"><svg width="10" height="12" viewBox="0 0 10 12"><path d="M5 0a4 4 0 0 1 4 4c0 3-4 8-4 8S1 7 1 4a4 4 0 0 1 4-4z" fill="#888"/><circle cx="5" cy="4" r="1.5" fill="#1d1d1d"/></svg>Brookvale, ST 00000 &nbsp;|&nbsp; P.O. Box 1187</div>
  <div class="f-info" style="top:1094px;font-size:12px;font-weight:600;color:#aaa"><svg width="11" height="11" viewBox="0 0 11 11"><path d="M2 0l2 3-1 1.5c.8 1.5 2 2.7 3.5 3.5L8 7l3 2-1.5 2C5 11 0 6 0 1.5z" fill="#888"/></svg>555-218-4470 <span style="font-weight:400;color:#666;font-size:10px">Or</span> 555-306-9152</div>

  <div class="abs footer-base"></div>
  <div class="abs donate">Donate Through:</div>
  <div class="pay" style="left:158px;background:#f2f2f2;color:#2a3d8f">PayEase</div>
  <div class="pay" style="left:196px;background:#f2f2f2;color:#333">Findcard</div>
  <div class="pay" style="left:234px;background:#f2f2f2;color:#1a2d8a">Vesta</div>
  <div class="pay" style="left:272px;background:#3d7cc4;color:#fff">Amerigo</div>
  <div class="pay" style="left:310px;background:#2a2a2a;color:#e88">Mastrio</div>
  <div class="abs copy">Copyright © 2014, WELCOME TO Harvest Gate Fellowship Network. All Rights Reserved.</div>
</footer>
</body>
</html>
```